Business card design for Virtual Assistance company

I need a business card designed for my virtual assistance company. We are a small company who services primarily C-level executive clients. The card needs to be double sided with the following contact information on the back:
Melissa Hartwell
Owner/CEO
info@pkrsolutions.net
www.pkrsolutions.net
310.552.9083

The front side should just have the company name incorporated: "PKR Solutions" and "virtual assistance"

The card should be simplistic, but eye catching and should speak to high level executives. Our primary focus areas consist of executive assistance and government contracting.

Target Market(s)

CEOs and executives

Contact Information for Business Card

see project description. phone, email, website.

Colors

Designer to choose only greyscale colors for use in the design.

```html
<!DOCTYPE html>
<html lang="en">
<head>
<meta charset="utf-8">
<title>PKR Solutions – Business Card</title>
<link href="https://fonts.googleapis.com/css2?family=Montserrat:wght@400;500;700&family=Lato:wght@400&display=swap" rel="stylesheet">
<style>
  :root {
    --stage: #2b2c2e;
    --card-dark: #232325;
    --card-light: #ffffff;
    --ink: #1c1c1e;
    --ink-soft: #7a7a7c;
    --rule: #d4d4d6;
    --on-dark: #f4f4f4;
    --on-dark-soft: #cfcfd1;
  }
  * { box-sizing: border-box; margin: 0; padding: 0; }
  html, body { width: 1200px; height: 952px; overflow: hidden; }
  body {
    background: var(--stage);
    display: flex;
    flex-direction: column;
    align-items: center;
    justify-content: center;
    gap: 56px;
  }
  .card {
    position: relative;
    width: 700px;
    height: 400px;
    overflow: hidden;
    box-shadow: 0 14px 30px rgba(0,0,0,.35);
  }

  /* Front side */
  .card--front {
    background: var(--card-dark);
    display: flex;
    flex-direction: column;
    align-items: center;
    justify-content: center;
  }
  .brand-name {
    font-family: "Montserrat", sans-serif;
    font-weight: 500;
    color: var(--on-dark);
    font-size: 40px;
    letter-spacing: 2px;
    white-space: nowrap;
  }
  .brand-tagline {
    margin-top: 6px;
    font-family: "Montserrat", sans-serif;
    font-weight: 400;
    color: var(--on-dark-soft);
    font-size: 19px;
    letter-spacing: 1px;
    white-space: nowrap;
  }

  /* Back side */
  .card--back { background: var(--card-light); }
  .edge-bar {
    position: absolute;
    width: 22px;
    height: 130px;
    background: var(--ink);
  }
  .edge-bar--left { left: 0; top: 0; }
  .edge-bar--right { right: 0; bottom: 0; }

  .identity {
    position: absolute;
    left: 50px;
    top: 0;
    width: 270px;
    height: 100%;
    display: flex;
    flex-direction: column;
    align-items: center;
    justify-content: center;
  }
  .identity .brand-name { color: var(--ink); font-size: 28px; letter-spacing: 1px; }
  .identity .brand-tagline {
    margin-top: 34px;
    color: var(--ink-soft);
    font-size: 11px;
    letter-spacing: 4px;
    text-transform: uppercase;
  }

  .divider {
    position: absolute;
    left: 382px;
    top: 70px;
    width: 1px;
    height: 160px;
    background: var(--rule);
    transform: rotate(20deg);
    transform-origin: top center;
  }

  .contact {
    position: absolute;
    left: 396px;
    top: 112px;
  }
  .contact-name {
    font-family: "Montserrat", sans-serif;
    font-size: 23px;
    color: var(--ink);
    text-transform: uppercase;
    letter-spacing: .5px;
    font-weight: 500;
    white-space: nowrap;
  }
  .contact-name strong { font-weight: 700; }
  .contact-role {
    font-family: "Lato", sans-serif;
    font-size: 17px;
    color: var(--ink-soft);
    margin: 2px 0 16px;
  }
  .contact-list { list-style: none; }
  .contact-list li {
    display: flex;
    align-items: center;
    gap: 10px;
    font-family: "Lato", sans-serif;
    font-size: 17px;
    color: var(--ink-soft);
    line-height: 26px;
    white-space: nowrap;
  }
  .contact-list svg { width: 14px; height: 14px; fill: var(--ink); flex: none; }
</style>
</head>
<body>

  <section class="card card--front" aria-label="Card front">
    <p class="brand-name">PKR Solutions</p>
    <p class="brand-tagline">virtual assistance</p>
  </section>

  <section class="card card--back" aria-label="Card back">
    <span class="edge-bar edge-bar--left"></span>
    <span class="edge-bar edge-bar--right"></span>

    <div class="identity">
      <p class="brand-name">PKR Solutions</p>
      <p class="brand-tagline">Virtual Assistance</p>
    </div>

    <span class="divider"></span>

    <div class="contact">
      <p class="contact-name">Melissa <strong>Hartwell</strong></p>
      <p class="contact-role">Owner/CEO</p>
      <ul class="contact-list">
        <li>
          <svg viewBox="0 0 24 24" aria-hidden="true"><path d="M6.6 10.8a15.1 15.1 0 0 0 6.6 6.6l2.2-2.2a1 1 0 0 1 1-.25 11.4 11.4 0 0 0 3.6.57 1 1 0 0 1 1 1V20a1 1 0 0 1-1 1A17 17 0 0 1 3 4a1 1 0 0 1 1-1h3.5a1 1 0 0 1 1 1c0 1.25.2 2.45.57 3.57a1 1 0 0 1-.25 1z"/></svg>
          310.552.9083
        </li>
        <li>
          <svg viewBox="0 0 24 24" aria-hidden="true"><path d="M2 5h20L12 13z"/><path d="M2 7l10 8 10-8v12H2z"/></svg>
          info@pkrsolutions.net
        </li>
        <li>
          <svg viewBox="0 0 24 24" aria-hidden="true"><circle cx="12" cy="12" r="10"/><path d="M2 12h20M12 2c3 3 3 17 0 20M12 2c-3 3-3 17 0 20" stroke="#fff" stroke-width="1.6" fill="none"/></svg>
          www.pkrsolutions.net
        </li>
      </ul>
    </div>
  </section>

</body>
</html>
```